Facebook Ad For New online Spectacle Store

We have started a new online store in Australia selling spectacles. As we don't have overheads such as rent electricity etc we are able to do these glasses at an extremely cheap price of $50 for the complete pair. We want to highlight the affordability and quality. This ad will be promoted on Facebook all over Australia. We want to make an impression. There are a lot of people wearing cheap magnifiers from chemists etc that are not suitable as most people need a corrective lens and rarely are both eyes the same power. So it's the people that are buying the $10 glasses we really want to sway to get ones that actually are the correct prescription for them without paying hundreds of dollars on a pair. "Throw away your magnifiers" As it's Facebook we can't really have too much writing in the image HOWEVER we want to highlight COMPLETE GLASSES $50 and that they will be the customers exact power lens. Our Website is www.lumaframe.com.au I have uploaded our logo but you do not need it in the design. We will be adding text to the Ad but not in the image you design (except for complete glasses for $50). you can take some of the images of frames from the website or I can upload just ask- tell me which one suits your design. Basically you have freedom to come up with something that will impress our potential customers make them click the link and check out our website.

Target Market(s)

People that use Cheap magnifiers - our glasses are a upgrade and better for their eyes

Industry/Entity Type

Eyewear

Colors

Designer to choose colors to be used in the design.

Requirements
Must have
• Complete Glasses $50 (Plus postage)- The (plus postage) in smaller writing than the Complete glasses for $50 part

```html
<!DOCTYPE html>
<html lang="en">
<head>
<meta charset="utf-8">
<title>Lumaframe – Throw Away Your Magnifiers</title>
<link rel="stylesheet" href="https://fonts.googleapis.com/css2?family=Oswald:wght@300;400&family=Raleway:wght@200&family=Montserrat:wght@500;700;800&display=swap">
<style>
  :root {
    --page: #4763a9;
    --paper: #ffffff;
    --sky: #37b3dc;
    --ring: #848484;
    --ink: #141414;
    --pill: #3b3b3b;
    --frame-light: #f1f1f1;
    --frame-mid: #dcdcdc;
  }
  html, body {
    margin: 0;
    padding: 0;
    overflow: hidden;
  }
  body {
    width: 1200px;
    height: 1200px;
    background: var(--page);
    display: flex;
    align-items: center;
    justify-content: center;
  }
  .ad {
    display: block;
    width: 1200px;
    height: 517px;
    background: var(--paper);
  }
  .headline-condensed { font-family: "Oswald", sans-serif; }
  .headline-thin { font-family: "Raleway", sans-serif; font-weight: 200; }
  .badge-text { font-family: "Montserrat", sans-serif; }
</style>
</head>
<body>
<svg class="ad" viewBox="0 0 1096 472" role="img" aria-label="Throw away your magnifiers – complete glasses $50 plus postage">
  <defs>
    <clipPath id="ring-clip">
      <rect x="0" y="0" width="455" height="472"/>
    </clipPath>
    <linearGradient id="frame-fill" x1="0" y1="0" x2="0" y2="1">
      <stop offset="0" stop-color="var(--frame-light)"/>
      <stop offset="1" stop-color="var(--frame-mid)"/>
    </linearGradient>
    <linearGradient id="pill-fill" x1="0" y1="0" x2="0" y2="1">
      <stop offset="0" stop-color="#555555"/>
      <stop offset="1" stop-color="var(--pill)"/>
    </linearGradient>
  </defs>

  <!-- blue field -->
  <rect class="sky-field" x="373" y="0" width="723" height="472" fill="var(--sky)"/>

  <!-- white headline bands -->
  <rect class="band-throw" x="373" y="55" width="285" height="92" fill="var(--paper)"/>
  <rect class="band-magnifiers" x="652" y="285" width="444" height="90" fill="var(--paper)"/>

  <!-- frame products -->
  <rect class="frame-gold" x="42" y="70" width="292" height="82" rx="30" fill="url(#frame-fill)" role="img" aria-label="Gold stainless steel aviator-style spectacle frame"/>
  <rect class="frame-navy" x="74" y="215" width="292" height="86" rx="32" fill="url(#frame-fill)" role="img" aria-label="Navy and tortoiseshell oval spectacle frame"/>

  <!-- price badge -->
  <circle class="badge-ring" cx="442" cy="336" r="162" fill="var(--ring)" clip-path="url(#ring-clip)"/>
  <circle class="badge-border" cx="442" cy="336" r="130" fill="var(--paper)"/>
  <circle class="badge-core" cx="442" cy="336" r="119" fill="var(--sky)"/>
  <g class="badge-text" fill="var(--paper)" text-anchor="middle">
    <text x="442" y="297" font-size="20" font-weight="700" textLength="150" lengthAdjust="spacingAndGlyphs">COMPLETE</text>
    <text x="442" y="322" font-size="20" font-weight="700" textLength="125" lengthAdjust="spacingAndGlyphs">GLASSES</text>
    <text x="442" y="372" font-size="50" font-weight="800" textLength="130" lengthAdjust="spacingAndGlyphs">$50</text>
    <text x="442" y="393" font-size="14" font-weight="700" fill="var(--ink)" textLength="118" lengthAdjust="spacingAndGlyphs">plus postage</text>
  </g>

  <!-- headline -->
  <text class="headline-condensed" x="421" y="130" font-size="84" font-weight="300" fill="var(--ink)" textLength="225" lengthAdjust="spacingAndGlyphs">THROW</text>
  <text class="headline-thin" x="651" y="185" font-size="182" fill="var(--paper)" textLength="415" lengthAdjust="spacingAndGlyphs">AWAY</text>
  <text class="headline-thin" x="516" y="270" font-size="98" fill="var(--paper)" textLength="225" lengthAdjust="spacingAndGlyphs">YOUR</text>
  <text class="headline-condensed" x="689" y="362" font-size="80" font-weight="300" fill="var(--ink)" textLength="332" lengthAdjust="spacingAndGlyphs">MAGNIFIERS</text>

  <!-- web address -->
  <rect class="url-pill" x="680" y="385" width="352" height="53" rx="6" fill="url(#pill-fill)"/>
  <text class="badge-text" x="856" y="418" font-size="21" font-weight="500" fill="var(--paper)" text-anchor="middle" letter-spacing="1">www.lumaframe.com.au</text>
</svg>
</body>
</html>
```